Direct Mail Postcard for new client solicitation

I need a postcard designed to market our full service accounting and financial services firm to local companies.

Our firm specializes in outsourced accounting and finance - we do everything from book keeping all the way up to financial oversight. We prefer to work on a flat fee recurring revenue basis rather than a traditional hourly fee. We also bring our own privately developed software to assist with the process. This software is proprietary in nature and not available elsewhere.

This card should convey:
1. Transferring financial headaches to a qualified company.
2. Stable access to help.
3. Cost savings.
4. A comprehensive package that allows for the client to take as much or as little as they would like.

I have attached our logo as a starting point. Feel free to engage us with questions and for guidance.

The company name is BrightLedgerCo.

Target Market(s)

the target market for this project is small businesses in the chicago area (our test market) with annual revenues between 5 and 10 Million dollars

Industry/Entity Type

Accounting

Font styles to use
Serif
Sans Serif

Requirements
Must have
• The project must convey the idea that we are taking administrative burdens and headaches from the client. The idea is that they are outsourcing their back office accounting functions to us while still retaining overall control of the process. The card must convey this concept somehow.
• We are also working on copy - since we are accountants and basically as boring as watching paint dry we are struggling a bit. Feel free to take a stab at copy as well. Keep in mind - we do not need to say alot - ideally we would say in essence "outsource your finance and accounting work to us for a reasonable fixed price".
Should not have
• We are reworking our website as well. The little orange guys and in fact the entire copy will be changing over the next few weeks. We would prefer to avoid using that motif for the card.

```html
<!DOCTYPE html>
<html lang="en">
<head>
<meta charset="utf-8">
<title>BrightLedgerCo Direct Mail Postcard</title>
<link rel="stylesheet" href="https://fonts.googleapis.com/css2?family=Arimo:wght@400;700&family=Questrial&display=swap">
<style>
  :root {
    --backdrop: #e9e6e1;
    --card-white: #ffffff;
    --sky-blue: #35aede;
    --deep-blue: #1a93c6;
    --leaf-green: #5fbd74;
    --lime-stripe: #c9d62c;
    --burst-orange: #f59a2c;
    --tick-orange: #f2ac2b;
    --line-grey: #b9b9b9;
    --photo-light: #d9d3c8;
    --photo-dark: #6d655c;
  }
  * { box-sizing: border-box; margin: 0; padding: 0; }
  html, body { width: 1200px; height: 800px; overflow: hidden; }
  body {
    background: var(--backdrop);
    position: relative;
    font-family: "Arimo", Arial, sans-serif;
  }
  .postcard {
    position: absolute;
    top: 215px;
    width: 560px;
    height: 370px;
    background: var(--card-white);
    box-shadow: 0 4px 14px rgba(0,0,0,0.18);
    overflow: hidden;
  }
  /* Message side */
  .postcard--message { left: 20px; }
  .message-panel {
    position: absolute;
    inset: 10px;
    background: var(--sky-blue);
  }
  .message-copy {
    position: absolute;
    left: 26px;
    top: 44px;
    width: 268px;
    color: var(--card-white);
    font-size: 12.4px;
    line-height: 1.33;
  }
  .message-copy p + p { margin-top: 14px; }
  .burst {
    position: absolute;
    left: 14px;
    top: 14px;
    width: 140px;
    height: 62px;
  }
  .burst-word {
    position: absolute;
    left: 40px;
    top: 28px;
    color: var(--card-white);
    font-size: 25px;
    line-height: 1;
  }
  .headline-lead { padding-left: 118px; display: block; }
  .divider-stripe {
    position: absolute;
    left: 306px;
    top: 0;
    bottom: 0;
    width: 5px;
    background: var(--lime-stripe);
  }
  .photo-area {
    position: absolute;
    left: 311px;
    top: 0;
    right: 0;
    bottom: 0;
    background: linear-gradient(160deg, var(--photo-light) 0%, #bdb4a7 45%, var(--photo-dark) 100%);
  }
  /* Address side */
  .postcard--address { left: 620px; }
  .offer-panel {
    position: absolute;
    left: 12px;
    top: 12px;
    bottom: 12px;
    width: 300px;
    background: var(--leaf-green);
    padding: 30px 0 0 30px;
    color: var(--card-white);
    font-family: "Questrial", "Century Gothic", sans-serif;
  }
  .slant-stripe {
    position: absolute;
    left: 300px;
    top: 12px;
    width: 40px;
    height: 346px;
  }
  .offer-title { font-size: 17px; line-height: 1.1; margin-left: 4px; }
  .service-list { list-style: none; margin-top: 2px; }
  .service-list li {
    display: flex;
    align-items: center;
    font-size: 16.5px;
    line-height: 18px;
    height: 19px;
  }
  .tick { width: 18px; height: 16px; margin-right: 4px; flex: none; }
  .offer-close { margin-top: 18px; font-size: 16.5px; line-height: 1.2; width: 240px; }
  .stamp-box {
    position: absolute;
    right: 40px;
    top: 52px;
    width: 56px;
    height: 64px;
    border: 1.5px solid #222;
  }
  .address-lines {
    position: absolute;
    left: 372px;
    top: 186px;
    width: 150px;
  }
  .address-lines span {
    display: block;
    height: 1px;
    background: var(--line-grey);
    margin-bottom: 21px;
  }
</style>
</head>
<body>

  <section class="postcard postcard--message" aria-label="Postcard message side">
    <div class="message-panel">
      <svg class="burst" viewBox="0 0 140 62" aria-hidden="true">
        <polygon fill="var(--burst-orange)" points="70,0 80,16 104,4 98,22 138,20 108,34 132,50 96,44 92,62 74,48 52,60 50,44 10,52 32,36 2,22 38,22 34,4 58,16"/>
      </svg>
      <span class="burst-word">Finally</span>
      <div class="message-copy">
        <p><span class="headline-lead">- a way to offload</span>those financial headaches without losing control!</p>
        <p>BrightLedgerCo is more than a consulting firm - we are a partner that provides a total solution to your financial headaches. BrightLedgerCo is revolutionary way to handle your businesses finances. Using proprietary tools that allow you to control and monitor the processing of data we provide the most comprehensive solution to all your accounting and finance issues! Now you can move just the issues you want - at prices you can afford.</p>
      </div>
      <div class="divider-stripe"></div>
      <div class="photo-area" role="img" aria-label="Photo of a tired business owner resting his head on open books and financial papers"></div>
    </div>
  </section>

  <section class="postcard postcard--address" aria-label="Postcard address side">
    <div class="offer-panel">
      <p class="offer-title">We can help with</p>
      <ul class="service-list">
        <li><svg class="tick" viewBox="0 0 18 16" aria-hidden="true"><path d="M2 9 L7 14 L16 2" fill="none" stroke="var(--tick-orange)" stroke-width="3.4" stroke-linecap="round" stroke-linejoin="round"/></svg>Financial management</li>
        <li><svg class="tick" viewBox="0 0 18 16" aria-hidden="true"><path d="M2 9 L7 14 L16 2" fill="none" stroke="var(--tick-orange)" stroke-width="3.4" stroke-linecap="round" stroke-linejoin="round"/></svg>Accounting</li>
        <li><svg class="tick" viewBox="0 0 18 16" aria-hidden="true"><path d="M2 9 L7 14 L16 2" fill="none" stroke="var(--tick-orange)" stroke-width="3.4" stroke-linecap="round" stroke-linejoin="round"/></svg>Book keeping</li>
        <li><svg class="tick" viewBox="0 0 18 16" aria-hidden="true"><path d="M2 9 L7 14 L16 2" fill="none" stroke="var(--tick-orange)" stroke-width="3.4" stroke-linecap="round" stroke-linejoin="round"/></svg>Forecasting</li>
        <li><svg class="tick" viewBox="0 0 18 16" aria-hidden="true"><path d="M2 9 L7 14 L16 2" fill="none" stroke="var(--tick-orange)" stroke-width="3.4" stroke-linecap="round" stroke-linejoin="round"/></svg>Reporting</li>
        <li><svg class="tick" viewBox="0 0 18 16" aria-hidden="true"><path d="M2 9 L7 14 L16 2" fill="none" stroke="var(--tick-orange)" stroke-width="3.4" stroke-linecap="round" stroke-linejoin="round"/></svg>Bank management</li>
        <li><svg class="tick" viewBox="0 0 18 16" aria-hidden="true"><path d="M2 9 L7 14 L16 2" fill="none" stroke="var(--tick-orange)" stroke-width="3.4" stroke-linecap="round" stroke-linejoin="round"/></svg>Fund raising</li>
        <li><svg class="tick" viewBox="0 0 18 16" aria-hidden="true"><path d="M2 9 L7 14 L16 2" fill="none" stroke="var(--tick-orange)" stroke-width="3.4" stroke-linecap="round" stroke-linejoin="round"/></svg>Business transition planning</li>
        <li><svg class="tick" viewBox="0 0 18 16" aria-hidden="true"><path d="M2 9 L7 14 L16 2" fill="none" stroke="var(--tick-orange)" stroke-width="3.4" stroke-linecap="round" stroke-linejoin="round"/></svg>Tax compliance</li>
      </ul>
      <p class="offer-close">If you have headaches we have solutions!</p>
    </div>
    <svg class="slant-stripe" viewBox="0 0 40 346" preserveAspectRatio="none" aria-hidden="true">
      <polygon fill="var(--deep-blue)" points="12,0 40,0 12,346 0,346 0,0"/>
    </svg>
    <div class="stamp-box" aria-label="Stamp area"></div>
    <div class="address-lines" aria-label="Address lines">
      <span></span><span></span><span></span><span></span><span></span>
    </div>
  </section>

</body>
</html>
```